Letterhead design for Dental Practice - Ashby Lane Dental Care

Letterhead for Private Dental Practice. To be used for all official correspondance and for printing treatment details on to be given to patients.

Target Market(s)

Private dental patients

Industry/Entity Type

Dental Clinic

Font styles to use
Other font styles liked:
• nexa-light

Colors
33a6d7
1c66ac
85abd2

Requirements
Must have
• info in the footer and header needs to be 3.5cm from upper/lower boader of paper, see photo in uploaded files
• info details:
• tel. 01632 960 418
• email info@ashbylanedc.co.uk
• ashbylanedentalcare.co.uk
• 17b Ashby Lane, Elmbridge Vale, Harrowfield HF4 7QT
• nexa-light font as in uploaded logo files
Should not have
• No funny tooth pictures

```html
<!DOCTYPE html>
<html lang="en">
<head>
<meta charset="utf-8">
<title>Ashby Lane Dental Care – Letterhead</title>
<link href="https://fonts.googleapis.com/css2?family=Roboto:wght@300;400&display=swap" rel="stylesheet">
<style>
  :root {
    --brand-blue: #139fd9;
    --accent-light: #33a6d7;
    --accent-deep: #1c66ac;
    --text-dark: #3c3c3e;
    --rule-grey: #58585a;
    --paper: #ffffff;
    --backdrop: #e9e7e4;
  }
  * { margin: 0; padding: 0; box-sizing: border-box; }
  html, body {
    width: 1200px;
    height: 1120px;
    overflow: hidden;
    background: var(--backdrop);
  }
  .letterhead {
    position: absolute;
    left: 191px;
    top: 20px;
    width: 817px;
    height: 1080px;
    background: var(--paper);
    box-shadow: 0 2px 10px rgba(0,0,0,0.15);
    overflow: hidden;
    font-family: 'Roboto', Arial, sans-serif;
  }
  .brand {
    position: absolute;
    left: 74px;
    top: 88px;
    display: flex;
    align-items: center;
    gap: 10px;
  }
  .brand-dot {
    width: 14px;
    height: 14px;
    border-radius: 50%;
    background: var(--brand-blue);
  }
  .brand-name {
    font-weight: 300;
    font-size: 22px;
    letter-spacing: 0.3px;
    color: var(--brand-blue);
  }
  .contact {
    position: absolute;
    left: 74px;
    top: 990px;
    font-size: 12.5px;
    line-height: 16.5px;
    color: var(--text-dark);
    letter-spacing: -0.1px;
  }
  .contact-line {
    display: flex;
    align-items: center;
    gap: 5px;
    white-space: nowrap;
  }
  .contact-icon {
    width: 10px;
    height: 10px;
    flex: none;
  }
  .divider {
    margin: 0 4px;
    color: var(--rule-grey);
  }
  .footer-band {
    position: absolute;
    left: 0;
    bottom: 0;
    width: 817px;
    height: 36px;
  }
</style>
</head>
<body>
  <main class="letterhead">
    <header class="brand">
      <span class="brand-dot"></span>
      <span class="brand-name">ashby lane dental care</span>
    </header>

    <footer class="contact">
      <div class="contact-line">
        <svg class="contact-icon" viewBox="0 0 10 10" aria-hidden="true">
          <path d="M2 1 C0.5 3 3 8.5 8 9 L9 7.5 L7 6.3 L6 7.2 C4.5 6.5 3.5 5.5 2.8 4 L3.7 3 L2.5 1Z" fill="var(--brand-blue)"/>
        </svg>
        <span>01632 960 418</span>
      </div>
      <div class="contact-line">
        <svg class="contact-icon" viewBox="0 0 10 10" aria-hidden="true">
          <rect x="0.5" y="2" width="9" height="6.5" fill="var(--brand-blue)"/>
          <path d="M0.5 2 L5 5.5 L9.5 2" fill="none" stroke="#fff" stroke-width="0.9"/>
        </svg>
        <span>info@ashbylanedc.co.uk</span>
        <span class="divider">|</span>
        <svg class="contact-icon" viewBox="0 0 10 10" aria-hidden="true">
          <circle cx="5" cy="5" r="4.3" fill="none" stroke="var(--brand-blue)" stroke-width="0.9"/>
          <ellipse cx="5" cy="5" rx="1.8" ry="4.3" fill="none" stroke="var(--brand-blue)" stroke-width="0.8"/>
          <path d="M0.7 5 H9.3" stroke="var(--brand-blue)" stroke-width="0.8"/>
        </svg>
        <span>ashbylanedentalcare.co.uk</span>
      </div>
      <div class="contact-line">
        <span>17b Ashby Lane, Elmbridge Vale, Harrowfield HF4 7QT</span>
      </div>
    </footer>

    <svg class="footer-band" viewBox="0 0 817 36" preserveAspectRatio="none" aria-hidden="true">
      <path d="M0 36 L0 24 L817 6 L817 36 Z" fill="var(--accent-light)"/>
      <path d="M0 36 L0 30 L817 18 L817 36 Z" fill="var(--accent-deep)"/>
    </svg>
  </main>
</body>
</html>
```